Business Intelligence Dashboard header

We are a top 10 cancer treatment clinic. Our analytics teams (Corporate Finance, Financial Analytics, and Clinical Analytics) are searching for a great graphic to show our business partners the value of our business intelligence products. We are hoping to convey that we are tech-savvy, supportive to our patients and mission of saving lives, valuable, forward-thinking, agile, supportive, and friendly.

This header will be placed at the top of each data visualization ('viz') that we create. We would like a design that is in-line with our company branding, simple, elegant, and striking. We primarily create headers that are between 800 and 1300 pixels across (800 and 1300 being the most common) and between 60 and 80 pixels high (76 being our current header height in px, but we are open to slight deviation.) The type of data visualizations this will sit atop (everything we produce, but just a few examples) will be things like patient safety, clinic utilization, appointment volumes, provider scorecards, and many more. I've included our current header, and a header I saw and liked (although I think it could have been a bit cooler.)

I'm open to ideas, feedback, and your opinion as a designer to come up with something amazing. You can find our website at https://www.brightharborhealth.org/
Googling our business shows our main clinic (with the rounded front) https://www.findwell.com/search?q=brightharbor+oncology+partners&source=lnms&tbm=isch&sa=X&ved=0ahUKEwjjws22xuLXAhVM5mMKHb82CpQQ_AUIDCgD&biw=1995&bih=916

We are open to stock images.

Requirements
Must have
• A place to write in a dashboard title (we will use our own BI-native object to float over the top of this banner)
Nice to have
• We would like a place/icon to differentiate between work products coming out of Clinical Analytics/Financial Analytics/Corporate Finance. We're fine with it being on 2 lines, or simply designing an icon to differentiate. We could use smaller text underneath the dashboard title (see must haves), an icon for each of the 3 teams, or a space in the header to write in the team ourselves. The team names should be of limited significance on the header. The star of the show will be the dashboard title (just leave an area for it) where the team names should be of less significance (off to the side, under the title in smaller font, etc)

```html
<!DOCTYPE html>
<html lang="en">
<head>
<meta charset="utf-8">
<title>Dashboard Header Set</title>
<link rel="stylesheet" href="https://fonts.googleapis.com/css2?family=Open+Sans:wght@300;400;600&display=swap">
<style>
  :root {
    --page-bg: #141414;
    --size-label: #2b2b2b;
    --brand-grey: #6e6561;
    --brand-yellow: #fec925;
    --brand-amber: #f3a41a;
    --team-orange: #b4600e;
    --team-text: #fde3a6;
    --name-text: #f4efe9;
  }
  * { box-sizing: border-box; margin: 0; padding: 0; }
  html, body { width: 1200px; height: 888px; overflow: hidden; }
  body {
    background: var(--page-bg);
    font-family: "Open Sans", Arial, sans-serif;
    position: relative;
  }
  .size-label {
    position: absolute;
    left: 79px;
    font-weight: 300;
    font-size: 27px;
    color: var(--size-label);
    letter-spacing: 0.5px;
  }
  .banner {
    position: absolute;
    left: 80px;
    height: 64px;
    background: var(--brand-grey);
    overflow: hidden;
  }
  .banner--wide { width: 1040px; }
  .banner--narrow { width: 800px; }

  .org-name {
    position: absolute;
    left: 14px;
    top: 0;
    height: 64px;
    display: flex;
    align-items: center;
    color: var(--name-text);
    font-weight: 400;
    font-size: 12px;
    line-height: 15px;
  }
  .title-field {
    position: absolute;
    left: 116px;
    top: 0;
    right: 0;
    height: 64px;
    background: var(--brand-yellow);
    border-bottom-left-radius: 46px 64px;
    box-shadow: -5px 0 0 var(--brand-amber);
  }
  .photo-strip {
    position: absolute;
    top: 0;
    height: 64px;
  }
  .banner--wide .photo-strip { left: 536px; width: 380px; }
  .banner--narrow .photo-strip { left: 452px; width: 240px; }
  .photo-strip--finance {
    background: linear-gradient(90deg, rgba(254,201,37,0) 0%, #f1b324 35%, #e0a021 70%, #c97a15 92%, var(--team-orange) 100%);
  }
  .photo-strip--clinic {
    background: linear-gradient(90deg, rgba(254,201,37,0) 0%, #eeb12a 30%, #e3a52a 70%, #c97a15 92%, var(--team-orange) 100%);
  }
  .photo-strip--chart {
    background: linear-gradient(90deg, rgba(254,201,37,0) 0%, #efa923 35%, #dc931c 70%, #c47215 92%, var(--team-orange) 100%);
  }
  .team-tag {
    position: absolute;
    top: 0;
    right: 0;
    height: 64px;
    background: var(--team-orange);
    display: flex;
    align-items: center;
    color: var(--team-text);
    font-weight: 400;
  }
  .banner--wide .team-tag { width: 124px; padding-left: 8px; font-size: 15px; line-height: 14.5px; }
  .banner--narrow .team-tag { width: 108px; padding-left: 6px; font-size: 12px; line-height: 12px; }
  .team-icon { flex: none; margin-right: 8px; }
  .banner--wide .team-icon { width: 28px; height: 28px; }
  .banner--narrow .team-icon { width: 23px; height: 23px; margin-right: 6px; }
</style>
</head>
<body>

<div class="size-label" style="top:50px;">1300 x 80</div>

<div class="banner banner--wide" style="top:100px;">
  <div class="title-field"></div>
  <div class="photo-strip photo-strip--finance" role="img" aria-label="Golden photo of coins and gears fading into the banner"></div>
  <div class="org-name">Bright Harbor<br>Health</div>
  <div class="team-tag">
    <svg class="team-icon" viewBox="0 0 28 28"><circle cx="14" cy="14" r="14" fill="#fec925"/><rect x="8" y="14" width="3" height="8" fill="#b4600e"/><rect x="13" y="9" width="3" height="13" fill="#b4600e"/><rect x="18" y="16" width="3" height="6" fill="#b4600e"/></svg>
    <span>Corporate<br>Finance</span>
  </div>
</div>

<div class="banner banner--wide" style="top:209px; left:81px;">
  <div class="title-field"></div>
  <div class="photo-strip photo-strip--clinic" role="img" aria-label="Golden photo of the main clinic with its rounded front"></div>
  <div class="org-name">Bright Harbor<br>Health</div>
  <div class="team-tag">
    <svg class="team-icon" viewBox="0 0 28 28"><circle cx="14" cy="14" r="14" fill="#fec925"/><polyline points="4,15 9,15 11,10 14,20 17,7 19,15 24,15" fill="none" stroke="#b4600e" stroke-width="2" stroke-linejoin="round"/></svg>
    <span>Clinical<br>Analytics</span>
  </div>
</div>

<div class="banner banner--wide" style="top:318px;">
  <div class="title-field"></div>
  <div class="photo-strip photo-strip--chart" role="img" aria-label="Golden photo of a financial line chart"></div>
  <div class="org-name">Bright Harbor<br>Health</div>
  <div class="team-tag">
    <svg class="team-icon" viewBox="0 0 28 28"><circle cx="14" cy="14" r="14" fill="#fec925"/><polyline points="5,19 10,13 15,17 22,8" fill="none" stroke="#b4600e" stroke-width="2.4" stroke-linejoin="round"/><circle cx="10" cy="13" r="2" fill="#b4600e"/><circle cx="15" cy="17" r="2" fill="#b4600e"/></svg>
    <span>Financial<br>Analytics</span>
  </div>
</div>

<div class="size-label" style="top:458px;">1000 x 80</div>

<div class="banner banner--narrow" style="top:509px;">
  <div class="title-field"></div>
  <div class="photo-strip photo-strip--finance" role="img" aria-label="Golden photo of coins and gears fading into the banner"></div>
  <div class="org-name">Bright Harbor<br>Health</div>
  <div class="team-tag">
    <svg class="team-icon" viewBox="0 0 28 28"><circle cx="14" cy="14" r="14" fill="#fec925"/><rect x="8" y="14" width="3" height="8" fill="#b4600e"/><rect x="13" y="9" width="3" height="13" fill="#b4600e"/><rect x="18" y="16" width="3" height="6" fill="#b4600e"/></svg>
    <span>Corporate<br>Finance</span>
  </div>
</div>

<div class="banner banner--narrow" style="top:618px; left:81px;">
  <div class="title-field"></div>
  <div class="photo-strip photo-strip--clinic" role="img" aria-label="Golden photo of the main clinic with its rounded front"></div>
  <div class="org-name">Bright Harbor<br>Health</div>
  <div class="team-tag">
    <svg class="team-icon" viewBox="0 0 28 28"><circle cx="14" cy="14" r="14" fill="#fec925"/><polyline points="4,15 9,15 11,10 14,20 17,7 19,15 24,15" fill="none" stroke="#b4600e" stroke-width="2" stroke-linejoin="round"/></svg>
    <span>Clinical<br>Analytics</span>
  </div>
</div>

<div class="banner banner--narrow" style="top:726px;">
  <div class="title-field"></div>
  <div class="photo-strip photo-strip--chart" role="img" aria-label="Golden photo of a financial line chart"></div>
  <div class="org-name">Bright Harbor<br>Health</div>
  <div class="team-tag">
    <svg class="team-icon" viewBox="0 0 28 28"><circle cx="14" cy="14" r="14" fill="#fec925"/><polyline points="5,19 10,13 15,17 22,8" fill="none" stroke="#b4600e" stroke-width="2.4" stroke-linejoin="round"/><circle cx="10" cy="13" r="2" fill="#b4600e"/><circle cx="15" cy="17" r="2" fill="#b4600e"/></svg>
    <span>Financial<br>Analytics</span>
  </div>
</div>

</body>
</html>
```